quiet meadow therapy (QMT)

I need to build a website for my therapy business.
There are two parts to the website
on the landing page; they choose whether they are therapists making a referral or patients needing more information.
After that, they are taken to their respective pages.
There is the textual information and a referral form on the therapist page, and on the patient page, the text is a bit different, and there will be a booking page on the patient page.
Visually minimal, it's a therapeutic website. I want it clean, clinical, and modern
colors: greenish blue or maybe orangish
PHP/html code
Updates

Hi everyone
I'm very sorry for the lack of responses to your designs. I am trying to work it out, but this platform has been a challenge for me.
I appreciate everyone's efforts, and I am unsure how to rate designs and move forward with the ones I like. There is a 5-star rating, but I don't understand how I'm supposed to politely say that it is not it without feeling like I'm going to affect someone's future rating negatively.
Please understand me. Thank you

Designs look the same

Target Market(s)

therapy and stress management

Industry/Entity Type

stress management therapy

Coding

Coded - Design and coding required

Number of Pages Required

5+ page

Font styles to use
Serif

Colors
0094D4
00A9DD
6FCCEA
C7EBF8
E9F6FB
00AB8E
00BBA5
67D7C9
C6EFE9
E9F9F6

Requirements
Must have
• landing page that that have 2 options. one for therapist another for patient

```html
<!DOCTYPE html>
<html lang="en">
<head>
<meta charset="utf-8">
<title>QMT — Quiet Meadow Therapy</title>
<link rel="stylesheet" href="https://fonts.googleapis.com/css2?family=Poppins:wght@400;500;600;700&display=swap">
<style>
:root{
  --teal:#14b5a5;
  --teal-dark:#0f9d8f;
  --teal-soft:#67d7c9;
  --orange:#f7941d;
  --ink:#333333;
  --text:#6b6b6b;
  --muted:#8a8a8a;
  --panel:#f3f3f3;
  --card:#f6f6f6;
  --footer:#2f2f2f;
  --white:#ffffff;
}
*{box-sizing:border-box;margin:0;padding:0}
html,body{width:1200px;height:4655px;overflow:hidden}
body{position:relative;font-family:"Poppins",sans-serif;color:var(--ink);background:var(--white)}
.abs{position:absolute}
.section-title{position:absolute;left:0;width:1200px;text-align:center;font-size:33px;font-weight:600;letter-spacing:.5px;text-transform:uppercase;color:var(--ink)}
.btn{position:absolute;display:flex;align-items:center;justify-content:center;border-radius:30px;font-size:14px;font-weight:600;text-decoration:none}
.btn-orange{background:var(--orange);color:var(--white)}
.btn-white{background:var(--white);color:var(--orange)}

/* Header / hero */
.hero{position:absolute;left:0;top:0;width:1200px;height:735px;background:linear-gradient(100deg,#8a7a66 0%,#7c8f86 28%,#6fa59d 52%,#3fb3a5 78%,#4cc1b1 100%)}
.brand{position:absolute;display:flex;align-items:center;gap:12px;font-weight:600;font-size:40px;letter-spacing:8px;color:var(--ink)}
.brand-dot{width:34px;height:34px;border-radius:50%;background:var(--teal)}
.nav{position:absolute;left:343px;top:40px;display:flex;font-size:13px;color:var(--ink)}
.nav a{position:absolute;white-space:nowrap;text-decoration:none;color:var(--ink)}
.nav a.active{color:var(--orange)}
.phone-btn{left:952px;top:25px;width:187px;height:49px;gap:8px;font-size:15px;font-weight:500}
.hero-title{position:absolute;right:61px;top:210px;text-align:right;font-size:60px;line-height:72px;font-weight:600;color:var(--white)}
.hero-text{position:absolute;right:61px;top:428px;width:460px;text-align:right;font-size:12px;line-height:24px;color:var(--white)}

/* Services */
.services-grid{position:absolute;left:0;top:930px;width:1200px}
.service{position:absolute;width:240px;text-align:center;font-size:14.5px;font-weight:500;color:#555}
.service svg{display:block;margin:0 auto 14px}

/* Help */
.help{position:absolute;left:0;top:1332px;width:1200px;height:466px;background:var(--panel)}
.help-art{position:absolute;left:54px;top:59px;width:524px;height:353px;border-radius:6px;background:linear-gradient(135deg,#f3f3f3 0%,#ece7df 50%,#e3efec 100%)}
.help h2{position:absolute;left:658px;top:88px;font-size:33px;font-weight:600;text-transform:uppercase}
.help p{position:absolute;left:658px;top:148px;width:430px;font-size:12.5px;line-height:24px;color:var(--text)}
.help .btn{left:658px;top:320px;width:314px;height:47px}

/* Team */
.team{position:absolute;left:0;top:1798px;width:1200px;height:594px;background:linear-gradient(180deg,#e9e8e4 0%,#dcdad4 45%,#5a6e7a 100%)}
.team .section-title{top:76px}
.team .btn{left:481px;top:464px;width:238px;height:47px}

/* FAQ */
.faq-title{top:2478px}
.faq-item{position:absolute;width:450px;background:var(--card);padding:0 20px;font-size:13px;font-weight:500;color:var(--ink)}
.faq-q{height:51px;display:flex;align-items:center;justify-content:space-between}
.faq-a{font-size:11px;line-height:21px;font-weight:400;color:var(--text);margin-top:-6px}
.sign{width:20px;height:20px;position:relative}
.sign::before,.sign::after{content:"";position:absolute;background:var(--teal)}
.sign::before{left:0;top:9px;width:20px;height:2px}
.sign.plus::after{left:9px;top:0;width:2px;height:20px}

/* Location */
.location{position:absolute;left:0;top:2900px;width:1200px;height:300px;background:var(--teal)}
.location .section-title{top:76px;color:var(--white)}
.map-card{position:absolute;left:188px;top:3068px;width:824px;height:410px;background:var(--white);box-shadow:0 2px 10px rgba(0,0,0,.08);padding:15px 16px 14px}
.map{width:100%;height:100%;background:linear-gradient(135deg,#eef0e4 0%,#e3e8d5 40%,#e9e6dc 70%,#dde7cf 100%)}
.divider{position:absolute;left:60px;top:3571px;width:1078px;height:1px;background:#e4e4e4}

/* News */
.news-title{top:3656px}
.news-card{position:absolute;top:3739px;width:338px;height:459px;background:var(--card)}
.news-img{height:224px}
.news-body{padding:26px 20px 0 22px}
.news-date{font-size:11.5px;color:var(--orange)}
.news-card h3{margin-top:10px;font-size:14px;line-height:26px;font-weight:600;color:var(--ink)}
.news-card p{margin-top:8px;font-size:10.5px;line-height:21px;color:var(--text)}
.read-more{display:block;margin-top:18px;font-size:12px;color:var(--orange);text-decoration:none}

/* Footer */
.footer{position:absolute;left:0;top:4286px;width:1200px;height:369px;background:var(--footer);color:#e6e6e6}
.footer h4{position:absolute;top:56px;font-size:12.5px;font-weight:600;color:var(--orange);text-transform:uppercase}
.footer .about{position:absolute;left:60px;top:130px;width:240px;font-size:11px;line-height:21px;color:#cfcfcf}
.socials{position:absolute;left:61px;top:197px;display:flex;gap:13px}
.socials span{width:40px;height:40px;border-radius:50%;border:1px solid #bdbdbd}
.socials span.on{background:var(--teal);border-color:var(--teal)}
.links{position:absolute;left:338px;top:78px;list-style:none;font-size:12px;line-height:30px}
.links a{color:#e6e6e6;text-decoration:none}
.contact-row{position:absolute;left:616px;display:flex;gap:10px;font-size:12px;line-height:22px;color:#e6e6e6}
.contact-row.phone{color:var(--teal-soft);font-size:14px;font-weight:500}
.newsletter p{position:absolute;left:893px;top:78px;width:250px;font-size:12px;line-height:22px}
.email-field{position:absolute;left:893px;top:138px;width:247px;height:40px;background:#3d3d3d;border:1px solid #4a4a4a;font-size:11.5px;color:#cfcfcf;display:flex;align-items:center;padding-left:10px}
.subscribe{position:absolute;left:893px;top:188px;width:247px;height:40px;background:var(--teal);color:var(--white);font-size:14px;font-weight:600;display:flex;align-items:center;justify-content:center}
.copyright{position:absolute;left:0;top:337px;width:1200px;text-align:center;font-size:11px;color:#cfcfcf}
.copyright b{font-weight:400;color:var(--orange)}
</style>
</head>
<body>

<header class="hero" role="img" aria-label="Photo of clasped hands resting on a railing beside a misty window, toned in warm brown fading to teal">
</header>
<div class="brand" style="left:60px;top:24px"><span class="brand-dot"></span>QMT</div>
<nav class="nav">
  <a class="active" style="left:0">HOME</a>
  <a style="left:71px">ABOUT</a>
  <a style="left:150px">SERVICES</a>
  <a style="left:242px">THERAPISTS</a>
  <a style="left:349px">PATIENTS</a>
  <a style="left:443px">BLOG</a>
  <a style="left:512px">CONTACT</a>
</nav>
<a class="btn btn-orange phone-btn">
  <svg width="15" height="15" viewBox="0 0 24 24"><path fill="#fff" d="M6.6 10.8a15.1 15.1 0 0 0 6.6 6.6l2.2-2.2c.3-.3.7-.4 1-.2 1.1.4 2.3.6 3.6.6.6 0 1 .4 1 1V20c0 .6-.4 1-1 1C10.6 21 3 13.4 3 4c0-.6.4-1 1-1h3.5c.6 0 1 .4 1 1 0 1.3.2 2.5.6 3.6.1.3 0 .7-.2 1z"/></svg>
  123 555 0142
</a>
<h1 class="hero-title">STRESS<br>THERAPY<br>BUSINESS</h1>
<p class="hero-text">Lorem Ipsum is simply dummy text of the printing and typesetting industry. Lorem Ipsum has been the industry's standard dummy text.</p>
<a class="btn btn-orange" style="left:848px;top:510px;width:148px;height:50px">Therapist</a>
<a class="btn btn-white" style="left:1012px;top:510px;width:127px;height:50px">Patient</a>

<!-- Services -->
<h2 class="section-title" style="top:820px">We offer services for...</h2>
<div class="services-grid">
  <div class="service" style="left:211px;top:0">
    <svg width="70" height="62" viewBox="0 0 70 62" fill="none" stroke="#14b5a5" stroke-width="2.4"><circle cx="20" cy="9" r="6"/><circle cx="35" cy="9" r="6"/><circle cx="50" cy="9" r="6"/><path d="M10 58V30a8 8 0 0 1 8-8h34a8 8 0 0 1 8 8v28M22 58V36M48 58V36M35 24v30"/></svg>
    Individual Counseling
  </div>
  <div class="service" style="left:480px;top:0">
    <svg width="70" height="62" viewBox="0 0 70 62" fill="none" stroke="#14b5a5" stroke-width="2.4"><circle cx="24" cy="14" r="8"/><circle cx="46" cy="16" r="8"/><path d="M6 54c0-12 8-20 18-20s18 8 18 20M30 54c2-10 8-16 16-16s14 6 16 16"/></svg>
    Couples Counseling
  </div>
  <div class="service" style="left:746px;top:0">
    <svg width="70" height="62" viewBox="0 0 70 62" fill="none" stroke="#14b5a5" stroke-width="2.4"><circle cx="20" cy="9" r="6"/><circle cx="50" cy="9" r="6"/><circle cx="35" cy="26" r="5"/><path d="M8 58V28a8 8 0 0 1 8-8h8a8 8 0 0 1 8 8M38 28a8 8 0 0 1 8-8h8a8 8 0 0 1 8 8v30M27 58V40a8 8 0 0 1 16 0v18"/></svg>
    Children &amp; Adolescents
  </div>
  <div class="service" style="left:198px;top:192px">
    <svg width="74" height="62" viewBox="0 0 74 62" fill="none" stroke="#14b5a5" stroke-width="2.4"><circle cx="14" cy="22" r="5"/><circle cx="30" cy="14" r="5"/><circle cx="46" cy="14" r="5"/><circle cx="60" cy="24" r="5"/><path d="M6 58V36a8 8 0 0 1 16 0v22M22 58V30a8 8 0 0 1 16 0v28M38 58V30a8 8 0 0 1 16 0v28M52 58V38a8 8 0 0 1 16 0v20"/></svg>
    Family Counseling
  </div>
  <div class="service" style="left:467px;top:192px">
    <svg width="70" height="62" viewBox="0 0 70 62" fill="none" stroke="#14b5a5" stroke-width="2.4"><circle cx="14" cy="6" r="5"/><path d="M14 12l-4 12 8 8M10 24l-8 4M14 16l10 4M4 58h62M28 56V40h8v16M40 56V30h8v26M52 56V18h8v38"/></svg>
    Executive Coaching
  </div>
  <div class="service" style="left:748px;top:192px">
    <svg width="66" height="62" viewBox="0 0 66 62" fill="none" stroke="#14b5a5" stroke-width="2.4"><circle cx="20" cy="8" r="5"/><circle cx="33" cy="8" r="5"/><circle cx="46" cy="8" r="5"/><circle cx="14" cy="26" r="5"/><circle cx="33" cy="26" r="5"/><circle cx="52" cy="26" r="5"/><path d="M4 58V42a8 8 0 0 1 8-8h42a8 8 0 0 1 8 8v16M16 58V44M50 58V44M33 34v22"/></svg>
    Groups
  </div>
</div>

<!-- How we can help -->
<section class="help">
  <div class="help-art" role="img" aria-label="Line illustration of a client in an orange shirt sitting on a couch talking with a therapist"></div>
  <h2>How we can help</h2>
  <p>Lorem Ipsum is simply dummy text of the printing and typesetting industry. Lorem Ipsum has been the industry's standard dummy text ever since the 1500s, when an unknown printer took a galley of type and scrambled it to make a type specimen book. It has survived not only five centuries, but also the leap into electronic typesetting, remaining essentially unchanged.</p>
  <a class="btn btn-orange">Schedule Your Free Consultation</a>
</section>

<!-- Team -->
<section class="team" role="img" aria-label="Group photo of five smiling team members standing together in a bright office">
  <h2 class="section-title">Meet our team</h2>
  <a class="btn btn-orange">View All Team Members</a>
</section>

<!-- FAQ -->
<h2 class="section-title faq-title">Frequently asked questions</h2>
<div class="faq-item" style="left:143px;top:2555px"><div class="faq-q">Lorem ipsum is simply dummy text?<span class="sign plus"></span></div></div>
<div class="faq-item" style="left:143px;top:2624px"><div class="faq-q">Lorem ipsum is simply dummy text?<span class="sign plus"></span></div></div>
<div class="faq-item" style="left:143px;top:2691px"><div class="faq-q">Lorem ipsum is simply dummy text?<span class="sign plus"></span></div></div>
<div class="faq-item" style="left:143px;top:2759px"><div class="faq-q">Lorem ipsum is simply dummy text?<span class="sign plus"></span></div></div>
<div class="faq-item" style="left:607px;top:2555px"><div class="faq-q">Lorem ipsum is simply dummy text?<span class="sign plus"></span></div></div>
<div class="faq-item" style="left:607px;top:2624px;height:117px"><div class="faq-q">Lorem ipsum is simply dummy text?<span class="sign"></span></div><p class="faq-a">Lorem Ipsum is simply dummy text of the printing and typesetting industry. Lorem Ipsum has been the industry's standard dummy text ever since the 1500s, when an unknown printer took a galley.</p></div>
<div class="faq-item" style="left:607px;top:2759px"><div class="faq-q">Lorem ipsum is simply dummy text?<span class="sign plus"></span></div></div>

<!-- Location -->
<section class="location"><h2 class="section-title">Find our location</h2></section>
<div class="map-card"><div class="map" role="img" aria-label="Road map of the practice's region"></div></div>
<div class="divider"></div>

<!-- News -->
<h2 class="section-title news-title">Our latest news</h2>
<article class="news-card" style="left:60px">
  <div class="news-img" role="img" aria-label="Photo of an autumn forest on a hillside" style="background:linear-gradient(180deg,#c9b9a4 0%,#a2703f 45%,#3e3a28 100%)"></div>
  <div class="news-body"><div class="news-date">04 Aug 2022</div><h3>Lorem ipsum is simply dummy text and printing typesetting.</h3><p>Lorem Ipsum is simply dummy text of the printing and typesetting industry. Lorem Ipsum has been the industry's standard dummy text ever since the 1500...</p><a class="read-more">READ MORE</a></div>
</article>
<article class="news-card" style="left:430px">
  <div class="news-img" role="img" aria-label="Photo of two women talking at a table by a bright window" style="background:linear-gradient(180deg,#e6e8ea 0%,#c9ccce 55%,#6b7a70 100%)"></div>
  <div class="news-body"><div class="news-date">03 Aug 2022</div><h3>Lorem ipsum is simply dummy text and printing typesetting.</h3><p>Lorem Ipsum is simply dummy text of the printing and typesetting industry. Lorem Ipsum has been the industry's standard dummy text ever since the 1500...</p><a class="read-more">READ MORE</a></div>
</article>
<article class="news-card" style="left:802px">
  <div class="news-img" role="img" aria-label="Photo of a person leaping joyfully in green mountains" style="background:linear-gradient(180deg,#c4c8c2 0%,#6f8363 50%,#3f5238 100%)"></div>
  <div class="news-body"><div class="news-date">02 Aug 2022</div><h3>Lorem ipsum is simply dummy text and printing typesetting.</h3><p>Lorem Ipsum is simply dummy text of the printing and typesetting industry. Lorem Ipsum has been the industry's standard dummy text ever since the 1500...</p><a class="read-more">READ MORE</a></div>
</article>

<!-- Footer -->
<footer class="footer">
  <div class="brand" style="left:60px;top:40px;color:#ffffff"><span class="brand-dot"></span>QMT</div>
  <p class="about">Lorem Ipsum is simply dummy text of the printing and typesetting industry.</p>
  <div class="socials"><span></span><span class="on"></span><span></span></div>

  <h4 style="left:338px">Quick links</h4>
  <ul class="links">
    <li><a>Home</a></li><li><a>About</a></li><li><a>Services</a></li><li><a>Therapists</a></li><li><a>Patients</a></li><li><a>Blog</a></li><li><a>Contact</a></li>
  </ul>

  <h4 style="left:616px">Contact info</h4>
  <div class="contact-row" style="top:78px">
    <svg width="14" height="18" viewBox="0 0 24 30" style="margin-top:8px;flex:none"><path fill="#14b5a5" d="M12 0a10 10 0 0 0-10 10c0 7.5 10 20 10 20s10-12.5 10-20A10 10 0 0 0 12 0zm0 14a4 4 0 1 1 0-8 4 4 0 0 1 0 8z"/></svg>
    <span>Lorem ipsum is simply dummy<br>text and printing.</span>
  </div>
  <div class="contact-row phone" style="top:143px">
    <svg width="15" height="15" viewBox="0 0 24 24" style="margin-top:3px"><path fill="#14b5a5" d="M6.6 10.8a15.1 15.1 0 0 0 6.6 6.6l2.2-2.2c.3-.3.7-.4 1-.2 1.1.4 2.3.6 3.6.6.6 0 1 .4 1 1V20c0 .6-.4 1-1 1C10.6 21 3 13.4 3 4c0-.6.4-1 1-1h3.5c.6 0 1 .4 1 1 0 1.3.2 2.5.6 3.6.1.3 0 .7-.2 1z"/></svg>
    123 555 0142
  </div>
  <div class="contact-row" style="top:189px">
    <svg width="15" height="12" viewBox="0 0 24 18" style="margin-top:5px"><path fill="#14b5a5" d="M0 0h24v18H0zm2 2v1l10 7 10-7V2z"/></svg>
    hello@qmt-care.com
  </div>

  <h4 style="left:893px">Newsletter</h4>
  <div class="newsletter"><p>Subscribe to stay with us and update our latest news, services, etc...</p></div>
  <div class="email-field">Enter email here...</div>
  <div class="subscribe">Subscribe Now</div>

  <p class="copyright">© <b>QMT</b> - 2022. All Rights Reserved.</p>
</footer>

</body>
</html>
```